BRAVO San Felipe - For all your home service needs.

I need a web site designed for my new business called BRAVO San Felipe. This business is for the repair and servicing of home appliances and air conditioning systems and for plumbing and electrical repairs at residences. We will offer 1 year service contracts that provide for unlimited service calls and repairs of the equipment that is enrolled in the program. The business is located in San Felipe, Baja CA, Mexico which has a large population of retired American and Canadians. These are our target audience, not the Mexican population.

The business is an outgrowth of another business we own in San Felipe called Cardon Property Services which has been in business for 7 years and is well known and highly regarded in the community. The company is owned and operated by two Mexican nationals and an American who are all full time residents of San Felipe.

Our business model is the same as an American company called Bravo whose web site is https://www.keelhomecare.net/.

I already have a domain on HostPerch called www.bravohomefix.com and need a web design to populate this domain. We also have a Logo designed which I will upload for you.

Target Market(s)

The target audience is American and Canadian retirees who own homes and live in San Felipe either part time or full time.

Industry/Entity Type

Air Conditioning

Requirements
Must have
• The web site must have a home page, about us, service contracts, repairs, AC sales, Renewals, Quotes and Contact us pages. The information will be very similar to that shown for https://www.keelhomecare.net/.
Nice to have
• San Felipe is a desert community with an ocean (the gulf of California) so the design should incorporate some desert motifs and some seaside motifs. Also, should have some thoughts about how are services will make living in San Felipe worry free and enable the clients to enjoy life. One number to call for all their home service needs.
Should not have
• Do not have anything that belittles Mexico or Mexicans.

```html
<!DOCTYPE html>
<html lang="en">
<head>
<meta charset="utf-8">
<title>Bravo - For all your home service needs.</title>
<link rel="stylesheet" href="https://fonts.googleapis.com/css2?family=Source+Sans+3:ital,wght@0,300;0,400;0,600;1,300&display=swap">
<style>
:root{
  --red:#c8192a;
  --red-dark:#a40f1e;
  --red-deep:#8e0c18;
  --ink:#333;
  --muted:#555;
  --line:#e2e2e2;
  --band:#f4f4f4;
  --white:#fff;
}
*{box-sizing:border-box;margin:0;padding:0}
html,body{width:1200px;height:1200px;overflow:hidden}
body{font-family:"Source Sans 3",sans-serif;color:var(--ink);position:relative;
  background:linear-gradient(180deg,#3f8fd0 0%,#8cc3ea 22%,#d8b27a 34%,#c78a45 60%,#b26a25 100%)}
.page{position:absolute;left:101px;top:24px;width:998px;height:1147px;background:var(--white);border-radius:6px;overflow:hidden}
.abs{position:absolute}
/* header */
.brand{left:117px;top:50px;display:flex;align-items:center;gap:10px}
.brand-dot{width:62px;height:62px;border-radius:50%;background:var(--red)}
.brand-name{font-size:40px;font-weight:600;color:var(--red)}
.call{left:806px;top:40px;display:flex;align-items:center;gap:8px;font-size:24px;font-weight:300;color:var(--muted)}
.call-icon{width:22px;height:22px;background:var(--red);border-radius:3px;display:flex;align-items:center;justify-content:center}
.call b{font-weight:300;color:var(--red)}
.social{left:684px;top:86px;display:flex;gap:6px}
.social span{width:34px;height:34px;border-radius:50%;background:var(--red)}
.social span:nth-child(even){background:#e0555f}
.search{left:850px;top:88px;width:222px;height:34px;border:1px solid #ddd;border-radius:4px;box-shadow:0 3px 4px rgba(0,0,0,.15);display:flex;align-items:center;font-size:14px;color:var(--muted);padding-left:16px}
.search-btn{position:absolute;right:0;top:-1px;width:31px;height:34px;background:var(--red);border-radius:0 4px 4px 0;display:flex;align-items:center;justify-content:center}
/* nav */
.nav{left:93px;top:147px;width:1014px;height:52px;background:linear-gradient(180deg,#d72434,var(--red-dark));border-radius:6px;display:flex;padding-left:24px;box-shadow:0 3px 5px rgba(0,0,0,.25)}
.nav a{color:var(--white);text-decoration:none;font-size:16.5px;font-weight:300;line-height:52px;padding:0 15.8px}
.nav a.active{background:var(--red-deep);padding:0 17px 0 22px}
/* hero */
.hero{left:101px;top:199px;width:997px;height:398px}
.hero-photo{position:absolute;inset:0;background:linear-gradient(135deg,#d9d4cc 0%,#eeebe4 40%,#b8b0a2 70%,#8f8678 100%)}
.hero-shape{position:absolute;inset:0}
.services{position:absolute;right:0;top:40px;width:333px}
.services li{list-style:none;height:76px;display:flex;align-items:center;justify-content:flex-end;gap:16px;padding-right:20px;color:var(--white);font-size:24px;font-weight:300;border-bottom:1px dashed rgba(255,255,255,.35)}
.services li.active{background:rgba(120,8,18,.45)}
.services li:last-child{border-bottom:none}
.dots-base{left:523px;top:592px;width:156px;height:17px;background:var(--red-dark);border-radius:0 0 6px 6px}
.dots{left:531px;top:572px;width:138px;height:34px;background:var(--red);border-radius:6px;display:flex;align-items:center;justify-content:center;gap:9px;padding-bottom:2px}
.dots span{width:12px;height:12px;border-radius:50%;background:#f1c7cb}
.dots span.on{background:var(--red-deep)}
/* welcome */
.welcome-title{left:117px;top:622px;font-size:20px;font-weight:300;color:var(--red)}
.welcome-text{left:117px;top:659px;width:399px;font-size:13.9px;line-height:18px;text-align:justify;color:#222;letter-spacing:-.1px}
.welcome-text p+p{margin-top:18px}
.btn{background:var(--red);color:var(--white);border-radius:5px;font-size:14px;display:flex;align-items:center;justify-content:center;box-shadow:0 2px 3px rgba(0,0,0,.2)}
.read-more{left:118px;top:874px;width:96px;height:33px}
.welcome-photo{left:537px;top:653px;width:222px;height:235px;border-radius:8px;border:1px solid #ddd;background:linear-gradient(135deg,#e9eef0,#cfd9dc 40%,#a9937c 75%,#d9cbb6)}
/* partners */
.divider{left:110px;top:926px;width:652px;height:1px;background:var(--line)}
.partners-title{left:135px;top:946px;font-size:20px;font-weight:300;color:var(--red)}
.badge{height:18px;border-radius:3px;background:#bdbdbd;top:950px}
/* quote form */
.quote{left:775px;top:610px;width:313px;height:357px;background:linear-gradient(180deg,var(--red),var(--red-dark));border-radius:6px}
.quote h2{position:absolute;left:20px;top:9px;font-size:26px;font-weight:300;color:var(--white)}
.quote-body{position:absolute;left:8px;top:50px;width:296px;height:297px;background:var(--white);border-radius:5px}
.field{position:absolute;left:11px;width:265px;border:1px solid #ccc;border-radius:4px;font-size:14.5px;font-style:italic;font-weight:300;color:#666;padding:8px 13px}
.field .caret{position:absolute;right:10px;top:15px;width:0;height:0;border-left:6px solid transparent;border-right:6px solid transparent;border-top:6px solid #666}
.quote-btn{left:857px;top:941px;width:152px;height:37px;font-size:16.5px;font-weight:300;border-radius:4px}
/* features */
.features{left:101px;top:1000px;width:998px;height:103px;background:var(--band)}
.feature{display:flex;align-items:center;gap:20px;color:var(--red);font-size:17px;line-height:19px}
/* footer */
.footer-nav{left:101px;top:1120px;width:998px;display:flex;justify-content:center;gap:27px;font-size:14px;color:var(--muted);padding-left:4px}
.copyright{left:101px;top:1146px;width:998px;text-align:center;font-size:13px;color:var(--red)}
</style>
</head>
<body>
<div class="page"></div>

<header>
  <div class="abs brand"><span class="brand-dot"></span><span class="brand-name">Bravo</span></div>
  <div class="abs call">
    <span class="call-icon"><svg width="12" height="14" viewBox="0 0 12 14"><path d="M3 1 L5 4 L3.6 5.4 Q5 8.6 7.6 10 L9 8.6 L11.5 10.6 L10 13 Q3 12 1 3 Z" fill="#fff"/></svg></span>
    <span>Call Us : <b>1800 . 410 . 726</b></span>
  </div>
  <div class="abs social" aria-label="Social links"><span></span><span></span><span></span><span></span></div>
  <div class="abs search">Search
    <span class="search-btn"><svg width="18" height="18" viewBox="0 0 18 18"><circle cx="7" cy="7" r="5" fill="none" stroke="#fff" stroke-width="2"/><line x1="10.6" y1="10.6" x2="16" y2="16" stroke="#fff" stroke-width="2.5" stroke-linecap="round"/></svg></span>
  </div>
</header>

<nav class="abs nav">
  <a class="active">Home</a><a>About us</a><a>Service</a><a>Contracts</a><a>Repairs</a><a>AC sales</a><a>Renewals</a><a>Quotes</a><a>Contact us</a>
</nav>

<section class="abs hero">
  <div class="hero-photo" role="img" aria-label="Bright modern white kitchen with steel worktops"></div>
  <svg class="hero-shape" width="997" height="398" viewBox="0 0 997 398">
    <path d="M750 0 Q660 70 630 190 Q622 320 760 398 L997 398 L997 0 Z" fill="#c8192a"/>
    <path d="M750 0 Q660 70 630 190" fill="none" stroke="#e25a66" stroke-width="2" opacity=".6"/>
  </svg>
  <ul class="services">
    <li class="active">Home Appliances <svg width="10" height="14"><path d="M8 0 L0 7 L8 14Z M8 2h2v10H8z" fill="#fff"/></svg></li>
    <li>Air Conditioning Systems <svg width="10" height="14"><path d="M8 0 L0 7 L8 14Z M8 2h2v10H8z" fill="#fff"/></svg></li>
    <li>Plumbing <svg width="10" height="14"><path d="M8 0 L0 7 L8 14Z M8 2h2v10H8z" fill="#fff"/></svg></li>
    <li>Electrical Repairs <svg width="10" height="14"><path d="M8 0 L0 7 L8 14Z M8 2h2v10H8z" fill="#fff"/></svg></li>
  </ul>
</section>
<div class="abs dots-base"></div>
<div class="abs dots"><span></span><span></span><span></span><span></span><span class="on"></span></div>

<main>
  <h1 class="abs welcome-title">Welcome to Our Website</h1>
  <div class="abs welcome-text">
    <p>Sed ut perspiciatis unde omnis iste natus error sit voluptatem accus-antium doloremque laudantium, totam rem aperiam, eaque ipsa quae ab illo inventore veritatis et quasi architecto beatae vitae dicta sunt explicabo. Nemo enim ipsam voluptatem quia voluptas sit aspernatur aut odit aut fugit, sed quia</p>
    <p>Sed ut perspiciatis unde omnis iste natus error sit voluptatem accus-antium doloremque laudantium, totam rem aperiam, eaque ipsa quae ab illo inventore veritatis et quasi architecto beatae vitae dicta sunt explicabo. Nemo enim ipsam voluptatem quia voluptas sit aspernatur aut odit aut fugit, sed quia</p>
  </div>
  <div class="abs btn read-more">Read more</div>
  <div class="abs welcome-photo" role="img" aria-label="Woman cleaning a kitchen appliance"></div>

  <div class="abs divider"></div>
  <h2 class="abs partners-title">Our Partners</h2>
  <span class="abs badge" style="left:276px;width:44px"></span>
  <span class="abs badge" style="left:347px;width:75px"></span>
  <span class="abs badge" style="left:448px;width:32px;height:22px;top:948px"></span>
  <span class="abs badge" style="left:522px;width:33px"></span>
  <span class="abs badge" style="left:593px;width:50px;height:14px;top:950px"></span>
  <span class="abs badge" style="left:679px;width:52px;height:14px;top:950px"></span>

  <aside class="abs quote">
    <h2>Quotes</h2>
    <div class="quote-body">
      <div class="field" style="top:13px;height:36px">Name</div>
      <div class="field" style="top:57px;height:36px">Email</div>
      <div class="field" style="top:101px;height:37px">Telephone</div>
      <div class="field" style="top:146px;height:36px">Do You Have an Active Contract&nbsp; *<span class="caret"></span></div>
      <div class="field" style="top:192px;height:74px;padding-top:10px">How Can We Help You?</div>
    </div>
  </aside>
  <div class="abs btn quote-btn">Get a FREE Quote</div>
</main>

<section class="abs features">
  <div class="abs feature" style="left:31px;top:33px">
    <svg width="28" height="24" viewBox="0 0 28 24"><rect x="0" y="3" width="17" height="13" fill="#c8192a"/><path d="M18 7h6l4 5v6H18z" fill="#c8192a"/><rect x="0" y="17" width="28" height="2" fill="#c8192a"/><circle cx="6" cy="21" r="3" fill="#c8192a" stroke="#f4f4f4"/><circle cx="22" cy="21" r="3" fill="#c8192a" stroke="#f4f4f4"/></svg>
    <span>Ready to dispatch<br>24/7 Service</span>
  </div>
  <div class="abs feature" style="left:273px;top:30px">
    <svg width="28" height="28" viewBox="0 0 28 28"><circle cx="14" cy="14" r="12" fill="none" stroke="#c8192a" stroke-width="2.5"/><path d="M8 14 l4 4 l8 -8" fill="none" stroke="#c8192a" stroke-width="2.5"/></svg>
    <span>Around the Clock<br>Service</span>
  </div>
  <div class="abs feature" style="left:514px;top:30px">
    <svg width="30" height="30" viewBox="0 0 30 30"><path d="M15 2 L28 8 L15 14 L2 8Z" fill="#c8192a"/><path d="M2 10 L14 16 L14 29 L2 23Z" fill="#c8192a"/><path d="M28 10 L16 16 L16 29 L28 23Z" fill="#a40f1e"/></svg>
    <span>Lowest Prices On<br>New AC Units</span>
  </div>
  <div class="abs feature" style="left:744px;top:30px">
    <svg width="26" height="28" viewBox="0 0 26 28"><path d="M22 16 A9 9 0 1 1 13 7 L13 3 L20 9 L13 15 L13 11 A5.5 5.5 0 1 0 18.5 16Z" fill="#c8192a"/></svg>
    <span>Quick Response Times<br>Since 1970</span>
  </div>
</section>

<footer>
  <div class="abs footer-nav"><span>Home</span><span>About us</span><span>Service</span><span>Contracts</span><span>Repairs</span><span>AC sales</span><span>Renewals</span><span>Quotes</span><span>Contact us</span></div>
  <div class="abs copyright">© 2013.www.bravohomefix.com</div>
</footer>
</body>
</html>
```